Australian Solar Smart Home Provider needs business card design

We need a simple, clean, business card that shows who we are and gives the brand feeling. Please see the website (www.pelvora.com) and the attached logo as well. Please use this logo on the business card. As a business we do residential solar, batteries, smart home technology, and hot water solutions. We want the feeling to be accessible to ages 40-65 but at the same time be a bit on the technologically savvy side.
Also the primary purpose of the business card is to hand of and drive referrals - so we want everyone to have a referral code on the card and that aspect should stand out.
Things we want on the card with an example employee:
Name: Brent Malvaney
Position: Director of Sales and Marketing
telephone number office: 02 8736 2914
telephone number mobile: 0478 591 830
address: Suite 403, 19 Clover Lane, Sydney, NSW 2000
website: www.pelvora.com
Target Market(s)
Homeowners aged 35-60
Industry/Entity Type
Residential
Contact Information for Business Card
Name: Brent Malvaney
website: www.pelvora.com
referral code: Bmalvaney
Look and feel

```html
<!DOCTYPE html>
<html lang="en">
<head>
<meta charset="utf-8">
<title>Pelvora Business Card</title>
<link href="https://fonts.googleapis.com/css2?family=Open+Sans:wght@400;600;700&display=swap" rel="stylesheet">
<style>
  :root {
    --backdrop: #e6e6e4;
    --card: #ffffff;
    --brand-green: #8cc63f;
    --text-grey: #6d6e70;
    --logo-grey: #8a8b8d;
    --circle-grey: #d7d8d9;
    --shadow: rgba(0, 0, 0, 0.16);
  }
  * { margin: 0; padding: 0; box-sizing: border-box; }
  html, body {
    width: 1200px;
    height: 576px;
    overflow: hidden;
    background: var(--backdrop);
    font-family: "Open Sans", Arial, sans-serif;
  }
  .stage {
    width: 1200px;
    height: 576px;
    display: flex;
    align-items: center;
    justify-content: center;
  }
  .business-card {
    position: relative;
    width: 820px;
    height: 500px;
    background: var(--card);
    border-radius: 26px;
    box-shadow: 0 10px 30px var(--shadow);
  }
  .brand {
    position: absolute;
    left: 64px;
    top: 58px;
    display: flex;
    align-items: center;
    gap: 16px;
  }
  .brand-dot {
    width: 62px;
    height: 62px;
    border-radius: 50%;
    background: var(--circle-grey);
  }
  .brand-name {
    font-size: 44px;
    font-weight: 700;
    color: var(--logo-grey);
    letter-spacing: -0.5px;
  }
  .person {
    position: absolute;
    right: 64px;
    top: 160px;
    text-align: right;
  }
  .person-name {
    font-size: 30px;
    font-weight: 700;
    color: var(--brand-green);
    letter-spacing: 0.3px;
  }
  .person-role {
    margin-top: 4px;
    font-size: 19px;
    color: var(--text-grey);
  }
  .contact-list {
    position: absolute;
    left: 64px;
    top: 262px;
    list-style: none;
  }
  .contact-item {
    display: flex;
    align-items: center;
    gap: 12px;
    height: 32px;
    font-size: 19px;
    color: var(--text-grey);
  }
  .contact-icon {
    width: 20px;
    height: 20px;
    flex: none;
    fill: var(--brand-green);
  }
  .referral {
    position: absolute;
    right: 64px;
    bottom: 52px;
    display: flex;
    align-items: center;
    gap: 14px;
    padding: 12px 22px;
    border-radius: 12px;
    background: var(--brand-green);
    color: var(--card);
  }
  .referral-label {
    font-size: 17px;
    font-weight: 400;
  }
  .referral-code {
    font-size: 24px;
    font-weight: 700;
    letter-spacing: 0.5px;
  }
</style>
</head>
<body>
<main class="stage">
  <section class="business-card">
    <div class="brand">
      <span class="brand-dot"></span>
      <span class="brand-name">pelvora</span>
    </div>

    <div class="person">
      <p class="person-name">Brent Malvaney</p>
      <p class="person-role">Director of Sales and Marketing</p>
    </div>

    <ul class="contact-list">
      <li class="contact-item">
        <svg class="contact-icon" viewBox="0 0 20 20" aria-hidden="true">
          <path d="M2 7c0-2 3-4 8-4s8 2 8 4v2h-4V7c-1-.6-2.4-1-4-1s-3 .4-4 1v2H2z"/>
          <rect x="4" y="10" width="12" height="7" rx="2"/>
        </svg>
        <span>02 8736 2914</span>
      </li>
      <li class="contact-item">
        <svg class="contact-icon" viewBox="0 0 20 20" aria-hidden="true">
          <path d="M5 2l3 4-2 2c1 2 3 4 5 5l2-2 4 3-2 3C9 17 3 11 2 5z"/>
        </svg>
        <span>0478 591 830</span>
      </li>
      <li class="contact-item">
        <svg class="contact-icon" viewBox="0 0 20 20" aria-hidden="true">
          <circle cx="10" cy="10" r="8"/>
          <path d="M2 10h16M10 2c-3 3-3 13 0 16M10 2c3 3 3 13 0 16" stroke="#fff" stroke-width="1.3" fill="none"/>
        </svg>
        <span>www.pelvora.com</span>
      </li>
      <li class="contact-item">
        <svg class="contact-icon" viewBox="0 0 20 20" aria-hidden="true">
          <path d="M10 2l9 8h-3v8h-4v-5H8v5H4v-8H1z"/>
        </svg>
        <span>Suite 403, 19 Clover Lane, Sydney, NSW 2000</span>
      </li>
    </ul>

    <div class="referral">
      <span class="referral-label">Referral code</span>
      <span class="referral-code">Bmalvaney</span>
    </div>
  </section>
</main>
</body>
</html>
```